Box packaging design for Pelko Cheese Knives Set

We would like a box design that is elegant and sophisticated. A box that would be great for gift giving. We are open to your creative ideas. Simple yet chic.

We also want a diagram of the 6 knives on the inside of the top of the lid to show what each knife is used for...you can see an example of it at the below link. We do not want to copy them...this is only for reference.

We will have text on the bottom of the box and "Made in China" somewhere on the box along with the UPC code. The 6 piece knife set is just like the Orvik set in the below link.

https://www.shopvarnel.example/ORVIK-Premium-6-Piece-Cheese-Knife/dp/Q73KD2XP9T/ref=sr_1_5?s=home-garden&ie=UTF8&qid=2084736215&sr=1-5&keywords=cheese+knives

Pelko, the name of our company means, "celebrate life."
Our company is all about the Home.
We specialize in very upscale, high-end products for dining, entertaining and cooking.

Attached is the logo that will go on the top of the box. (RGB pelko.eps)
WE WILL NOT BE USING THE TEXT - (Accessories for Sophisticated Chefs) ONLY the Word Pelko and the Z.

Attached is a picture of the set of cheese knives that will be going into
the box you will be designing. (Pic of cheese knives.jpg)

Also, attached is a product that we will be selling along with the cheese
knives which will be a second box to design to go along with the first one.
(Cheese marker 5 piece set).

The cheese knife insert card will also need to be designed to go inside the
box. (Cheese knife insert card.png)

On the back of the box we will provide you with a UPC code and where the
UPC code is...please type Made in China as show in the attachment. (UPS
code with Made in China)

Also, on the back of the box ..please add the attached text.

Good luck and best wishes!

1. The Pelko logo goes on the top of the box.
2. On the inside top of the box we want a diagram of the cheese knives similar to the below link but we can't copy it...if you also look at the card insert attached in the original project instructions you can see the diagram there.

Inside the top of the box will show each knife and what each knife does, for example. Do a silhouette of the knives and under each one will have text with what they are used for.... such as: Hard - Soft - Spread - Serving Fork - etc.

https://lnkvo.example/images/73bRtq

3. Bottom of box is the same as top size...see attached template for cheese knives box template.... Some text will be on the bottom which i will upload shortly and a UPC code in lower right hand corner with Made in China on it...see attached UPC code for reference.

I attached the cheese marker box template and the insert card template.

Let me know if you have any other questions....and best wishes...Marta

Target Market(s)

Our target audience are people who love to cook, entertain and celebrate life, high-end consumer catering to the luxury market.

Industry/Entity Type

Cooking

Colors
9bcb3b
abd036

Requirements
Must have
• simple yet sophisticated and chic
Nice to have
• We are open to your ideas ...
Should not have
• You can see the attached templates....PLEASE NOTE....the cheese marker template is NOT our design on it...they only sent this over to use the actual template.

```html
<!DOCTYPE html>
<html lang="en">
<head>
<meta charset="utf-8">
<title>Pelko Cheese Knife Set – Box Dielines</title>
<link rel="stylesheet" href="https://fonts.googleapis.com/css2?family=Montserrat:wght@400;600;700&family=Open+Sans:wght@400&display=swap">
<style>
  :root {
    --bg-center: #fbfbfb;
    --bg-edge: #d9d9d9;
    --lime: #b8f60c;
    --lime-line: #abd036;
    --ink: #000000;
    --fold: #3a3a3a;
    --paper-text: #ffffff;
    --caption: #222222;
    --pattern-light: #9a9a9a;
    --pattern-dark: #5c5c5c;
  }
  html, body {
    margin: 0;
    padding: 0;
    width: 1200px;
    height: 900px;
    overflow: hidden;
  }
  body {
    background: radial-gradient(ellipse at 50% 45%, var(--bg-center) 0%, var(--bg-edge) 100%);
    font-family: "Open Sans", Arial, sans-serif;
  }
  .board {
    position: relative;
    width: 1200px;
    height: 900px;
  }
  .board svg { position: absolute; overflow: visible; }
  .caption {
    position: absolute;
    margin: 0;
    color: var(--caption);
    font-size: 16px;
    transform: translateX(-50%);
    white-space: nowrap;
  }
  .caption--large { font-size: 19px; }
  .box-text { font-family: "Montserrat", Arial, sans-serif; fill: var(--paper-text); }
</style>
</head>
<body>
<main class="board">

  <!-- Foxing band -->
  <svg class="foxing-strip" style="left:0;top:0" width="1200" height="120" viewBox="0 0 1200 120">
    <polygon points="10,18 1180,18 1188,30 1188,101 1180,113 10,113" fill="var(--lime)"/>
    <g stroke="var(--ink)" stroke-width="1.2">
      <line x1="398" y1="18" x2="398" y2="25"/><line x1="398" y1="106" x2="398" y2="113"/>
      <line x1="592" y1="18" x2="592" y2="25"/><line x1="592" y1="106" x2="592" y2="113"/>
      <line x1="978" y1="18" x2="978" y2="25"/><line x1="978" y1="106" x2="978" y2="113"/>
      <line x1="1180" y1="18" x2="1180" y2="25"/><line x1="1180" y1="106" x2="1180" y2="113"/>
    </g>
  </svg>
  <p class="caption" style="left:643px;top:117px">green middle</p>

  <!-- Lid outside -->
  <svg class="dieline dieline--lid-outside" style="left:23px;top:144px" width="523" height="329" viewBox="0 0 523 329">
    <defs>
      <linearGradient id="patternTone" x1="0" y1="0" x2="1" y2="1">
        <stop offset="0" stop-color="var(--pattern-light)"/>
        <stop offset="1" stop-color="var(--pattern-dark)"/>
      </linearGradient>
    </defs>
    <g fill="var(--ink)">
      <rect x="68" y="0" width="387" height="329"/>
      <polygon points="34,40 68,34 68,68 34,68"/><polygon points="455,34 489,40 489,68 455,68"/>
      <polygon points="34,262 68,262 68,295 34,289"/><polygon points="455,262 489,262 489,289 455,295"/>
      <rect x="0" y="68" width="523" height="194"/>
    </g>
    <g role="img" aria-label="Black and white chevron zigzag pattern">
      <rect x="68" y="34" width="132" height="262" fill="url(#patternTone)"/>
      <rect x="323" y="34" width="132" height="262" fill="url(#patternTone)"/>
      <rect x="0" y="68" width="68" height="194" fill="url(#patternTone)"/>
      <rect x="455" y="68" width="68" height="194" fill="url(#patternTone)"/>
    </g>
    <g stroke="var(--fold)" stroke-width="0.8" fill="none">
      <line x1="68" y1="34" x2="455" y2="34"/><line x1="68" y1="296" x2="455" y2="296"/>
      <line x1="34" y1="68" x2="34" y2="262"/><line x1="489" y1="68" x2="489" y2="262"/>
    </g>
    <rect x="246" y="106" width="30" height="30" fill="var(--lime)"/>
    <text class="box-text" x="261" y="172" text-anchor="middle" font-size="20" font-weight="600" letter-spacing="6">PELKO</text>
    <rect role="img" aria-label="Silhouettes of the six cheese knives" x="209" y="194" width="108" height="28" fill="#2a2a2a"/>
    <g class="box-text" font-size="2.6" text-anchor="middle">
      <text x="213" y="232">ALMOND</text><text x="231" y="232">THIN</text><text x="250" y="232">SPREAD</text>
      <text x="270" y="232">PRONG</text><text x="290" y="232">FORK</text><text x="311" y="232">CHISEL</text>
    </g>
  </svg>
  <p class="caption" style="left:284px;top:478px">Inside the top of the box</p>

  <p class="caption caption--large" style="left:812px;top:422px">shoulder type box with inner foxing</p>

  <!-- Lid inside -->
  <svg class="dieline dieline--lid-inside" style="left:23px;top:527px" width="523" height="329" viewBox="0 0 523 329">
    <g fill="var(--ink)">
      <rect x="68" y="0" width="387" height="329"/>
      <polygon points="34,40 68,34 68,68 34,68"/><polygon points="455,34 489,40 489,68 455,68"/>
      <polygon points="34,262 68,262 68,295 34,289"/><polygon points="455,262 489,262 489,289 455,295"/>
      <rect x="0" y="68" width="523" height="194"/>
    </g>
    <g stroke="var(--fold)" stroke-width="0.8" fill="none">
      <line x1="68" y1="34" x2="455" y2="34"/><line x1="68" y1="296" x2="455" y2="296"/>
      <line x1="34" y1="68" x2="34" y2="262"/><line x1="489" y1="68" x2="489" y2="262"/>
      <line x1="68" y1="34" x2="68" y2="296"/><line x1="455" y1="34" x2="455" y2="296"/>
    </g>
    <rect x="150" y="77" width="16" height="13" fill="var(--lime)"/>
    <text class="box-text" x="158" y="101" text-anchor="middle" font-size="8" font-weight="600" letter-spacing="2.5">PELKO</text>
    <rect class="knife-frame" x="138" y="107" width="246" height="115" fill="none" stroke="var(--lime-line)" stroke-width="1"/>
    <rect role="img" aria-label="Outline drawings of the six cheese knives" x="150" y="122" width="222" height="64" fill="#2a2a2a"/>
    <g class="box-text" font-size="5" font-weight="700" text-anchor="middle">
      <text x="165" y="198">ALMOND</text><text x="165" y="205">KNIFE</text>
      <text x="204" y="198">THIN</text><text x="204" y="205">KNIFE</text>
      <text x="241" y="198">SPREADER</text><text x="241" y="205">KNIFE</text>
      <text x="279" y="198">PRONGED</text><text x="279" y="205">KNIFE</text>
      <text x="316" y="198">SERVING</text><text x="316" y="205">FORK</text>
      <text x="354" y="198">CHISEL</text><text x="354" y="205">KNIFE</text>
    </g>
    <text class="box-text" x="261" y="235" text-anchor="middle" font-size="5" font-weight="700" letter-spacing="2.6">PREMIUM 6 PIECE CHEESE KNIFE SET</text>
  </svg>
  <p class="caption" style="left:284px;top:860px">On the inside top</p>

  <!-- Box base -->
  <svg class="dieline dieline--base" style="left:633px;top:527px" width="523" height="329" viewBox="0 0 523 329">
    <g fill="var(--ink)">
      <rect x="68" y="0" width="387" height="329"/>
      <polygon points="34,40 68,34 68,68 34,68"/><polygon points="455,34 489,40 489,68 455,68"/>
      <polygon points="34,262 68,262 68,295 34,289"/><polygon points="455,262 489,262 489,289 455,295"/>
      <rect x="0" y="68" width="523" height="194"/>
    </g>
    <g stroke="var(--fold)" stroke-width="0.8" fill="none">
      <line x1="68" y1="34" x2="455" y2="34"/><line x1="68" y1="296" x2="455" y2="296"/>
      <line x1="34" y1="68" x2="34" y2="262"/><line x1="489" y1="68" x2="489" y2="262"/>
      <line x1="68" y1="34" x2="68" y2="296"/><line x1="455" y1="34" x2="455" y2="296"/>
    </g>
    <rect x="247" y="101" width="24" height="22" fill="var(--lime)"/>
    <text class="box-text" x="262" y="146" text-anchor="middle" font-size="12" font-weight="600" letter-spacing="4">PELKO</text>
    <text class="box-text" x="262" y="153" text-anchor="middle" font-size="2.8" font-weight="600" letter-spacing="1">ACCESSORIES FOR SOPHISTICATED CHEFS</text>
    <g class="box-text" font-size="5.3" text-anchor="middle">
      <text x="262" y="168"><tspan font-weight="700">Pelko</tspan> means - celebrate life! Nothing says “celebrate” quite like good food,</text>
      <text x="262" y="178">good friends and good cheer! Inspired by our love for cooking, we here at</text>
      <text x="262" y="188"><tspan font-weight="700">Pelko</tspan> want to share our passion and excitement by providing you with the</text>
      <text x="262" y="198">finest quality accessories for entertaining. It’s all about creating great</text>
      <text x="262" y="208">memories by bringing family and friends together while enjoying good food.</text>
      <text x="262" y="227">Celebrate life and enjoy the moment!</text>
    </g>
    <g class="care-icons" fill="none" stroke="var(--paper-text)" stroke-width="1.4">
      <circle cx="387" cy="246" r="5"/>
      <path d="M400 241 h9 M401 243 l1 9 h5 l1 -9"/>
    </g>
  </svg>
  <p class="caption" style="left:894px;top:860px">Bottom of the box</p>

</main>
</body>
</html>
```